Option Sheet

We need a one page option sheet with a left to right reading of the five options. It should be a one sheet, multiple colors and definitive separations between options This is used in a sales consultation. Backround or colors not in option need to have the follow RGB value (5 red, 20 green, 63 blue)

We added a smaller text file, please change that point

Target Market(s)

Divorce

Industry/Entity Type

Legal

Requirements
Must have
• 1) All five options left to right
• 2)language included in sheet

```html
<!DOCTYPE html>
<html lang="en">
<head>
<meta charset="utf-8">
<title>Five Options Divorce</title>
<link href="https://fonts.googleapis.com/css2?family=Montserrat:wght@700;800&family=Source+Sans+3:wght@400;600;700&display=swap" rel="stylesheet">
<style>
  :root {
    --navy: rgb(5, 20, 63);
    --red: #a6192e;
    --red-dark: #8a1124;
    --orange: #e8451f;
    --orange-dark: #c93a17;
    --sky: #3a9ad9;
    --sky-dark: #2a86c4;
    --blue: #1a5ca8;
    --blue-dark: #124a8c;
    --green: #1e8a3a;
    --green-dark: #17722f;
    --paper: #ffffff;
    --ink: rgb(5, 20, 63);
  }
  * { box-sizing: border-box; margin: 0; padding: 0; }
  html, body { width: 1200px; height: 927px; overflow: hidden; background: var(--paper); }
  .sheet { position: relative; width: 1200px; height: 927px; background: var(--paper); font-family: "Source Sans 3", Arial, sans-serif; color: var(--ink); }
  .sheet-title {
    position: absolute; top: 44px; left: 0; width: 100%; text-align: center;
    font-family: "Montserrat", Arial, sans-serif; font-weight: 800; font-size: 42px; letter-spacing: 2px; color: var(--navy);
  }
  .option { position: absolute; top: 0; width: 164px; height: 927px; --tone: var(--navy); --tone-dark: var(--navy); }
  .option--nothing { left: 78px; --tone: var(--red); --tone-dark: var(--red-dark); }
  .option--counseling { left: 295px; --tone: var(--orange); --tone-dark: var(--orange-dark); }
  .option--diy { left: 512px; --tone: var(--sky); --tone-dark: var(--sky-dark); }
  .option--limited { left: 729px; --tone: var(--blue); --tone-dark: var(--blue-dark); }
  .option--hire { left: 945px; --tone: var(--green); --tone-dark: var(--green-dark); }

  .option-icon { position: absolute; top: 140px; left: 32px; width: 104px; height: 104px; }
  .option-number {
    position: absolute; top: 130px; left: 13px; width: 38px; height: 38px; border-radius: 50%;
    background: var(--paper); border: 4px solid var(--tone-dark); color: var(--tone-dark);
    font-family: "Montserrat", Arial, sans-serif; font-weight: 800; font-size: 20px; line-height: 30px; text-align: center;
  }
  .option-name {
    position: absolute; top: 262px; left: -30px; width: 224px; text-align: center;
    font-family: "Source Sans 3", Arial, sans-serif; font-weight: 700; font-size: 27px; line-height: 31px; color: var(--tone);
  }
  .label {
    position: absolute; left: 0; width: 164px; height: 29px; background: var(--tone); color: var(--paper);
    font-size: 18px; line-height: 29px; padding-left: 10px; font-weight: 400;
  }
  .label--pros { top: 348px; }
  .label--cons { top: 505px; }
  .option--hire .label--cons { top: 610px; }
  .label sup { font-size: 11px; margin-right: 3px; }
  .points { position: absolute; left: 12px; width: 150px; list-style: none; font-size: 14px; line-height: 17px; color: var(--ink); }
  .points li { position: relative; padding-left: 12px; }
  .points li::before { content: ""; position: absolute; left: 0; top: 6px; width: 5px; height: 5px; border-radius: 50%; background: var(--ink); }
  .points--pros { top: 388px; }
  .points--cons { top: 545px; }
  .option--hire .points--cons { top: 650px; }
</style>
</head>
<body>
<main class="sheet">
  <h1 class="sheet-title">Five Options Divorce</h1>

  <section class="option option--nothing">
    <svg class="option-icon" viewBox="0 0 104 104" aria-hidden="true">
      <circle cx="52" cy="52" r="50" fill="var(--red)"/>
      <circle cx="52" cy="52" r="26" fill="none" stroke="#fff" stroke-width="5"/>
      <line x1="34" y1="34" x2="70" y2="70" stroke="#fff" stroke-width="5"/>
    </svg>
    <div class="option-number">1</div>
    <h2 class="option-name">Do<br>Nothing</h2>
    <div class="label label--pros"><sup>+</sup>Advantages</div>
    <ul class="points points--pros"><li>Stay married</li><li>No life Changes</li></ul>
    <div class="label label--cons">- Disadvantages</div>
    <ul class="points points--cons"><li>Remain unhappy, depressed, anxious</li><li>Money and assets may disappear</li><li>What is going to change?</li></ul>
  </section>

  <section class="option option--counseling">
    <svg class="option-icon" viewBox="0 0 104 104" aria-hidden="true">
      <circle cx="52" cy="52" r="50" fill="var(--orange)"/>
      <path d="M52 27a24 24 0 1 1-12 45l-12 5 4-11A24 24 0 0 1 52 27z" fill="none" stroke="#fff" stroke-width="5" stroke-linejoin="round"/>
    </svg>
    <div class="option-number">2</div>
    <h2 class="option-name">Go to<br>Counseling</h2>
    <div class="label label--pros"><sup>+</sup>Advantages</div>
    <ul class="points points--pros"><li>Reconcile marriage</li><li>Help make a better life</li></ul>
    <div class="label label--cons">- Disadvantages</div>
    <ul class="points points--cons"><li>Past issues are highlighted and may drudge up old wounds</li><li>It may just clarify the reasons you need to separate and/or divorce</li><li>Both parties must be invested and willing to participate</li></ul>
  </section>

  <section class="option option--diy">
    <svg class="option-icon" viewBox="0 0 104 104" aria-hidden="true">
      <circle cx="52" cy="52" r="50" fill="var(--sky)"/>
      <circle cx="52" cy="42" r="12" fill="none" stroke="#fff" stroke-width="4.5"/>
      <path d="M32 74c2-12 10-18 20-18s18 6 20 18z" fill="none" stroke="#fff" stroke-width="4.5" stroke-linejoin="round"/>
    </svg>
    <div class="option-number">3</div>
    <h2 class="option-name">Do it<br>Yourself</h2>
    <div class="label label--pros"><sup>+</sup>Advantages</div>
    <ul class="points points--pros"><li>No attorney fees</li><li>You are your on attorney</li></ul>
    <div class="label label--cons">- Disadvantages</div>
    <ul class="points points--cons"><li>People often find that what is “fair,” may in fact, not be truly fair</li><li>Often times, people do not know the risks</li><li>Complicated legal system with intrigue rules</li><li>Unsure how to complete the necessary paperwork and meet the deadlines</li></ul>
  </section>

  <section class="option option--limited">
    <svg class="option-icon" viewBox="0 0 104 104" aria-hidden="true">
      <circle cx="52" cy="52" r="50" fill="var(--blue)"/>
      <path d="M52 26L77 72H27z" fill="none" stroke="#fff" stroke-width="4.5" stroke-linejoin="round"/>
      <line x1="52" y1="42" x2="52" y2="58" stroke="#fff" stroke-width="5"/>
      <circle cx="52" cy="65" r="3" fill="#fff"/>
    </svg>
    <div class="option-number">4</div>
    <h2 class="option-name">Limited<br>Representation</h2>
    <div class="label label--pros"><sup>+</sup>Advantages</div>
    <ul class="points points--pros"><li>Balance between going alone and our limited involvement in the case</li></ul>
    <div class="label label--cons">- Disadvantages</div>
    <ul class="points points--cons"><li>Our terms may not benefit from our legal knowledge</li><li>The legal consequences of your legal documents will not be explained to you so that you can formulate a plan for handling the rest of your case.</li><li>Your spouse or other parties may cause your legal fees to increase significantly without action on your part</li></ul>
  </section>

  <section class="option option--hire">
    <svg class="option-icon" viewBox="0 0 104 104" aria-hidden="true">
      <circle cx="52" cy="52" r="50" fill="var(--green)"/>
      <path d="M52 26l7.6 16.4 17.9 2-13.3 12.2 3.6 17.7L52 65.4l-15.8 8.9 3.6-17.7-13.3-12.2 17.9-2z" fill="#fff"/>
    </svg>
    <div class="option-number">5</div>
    <h2 class="option-name">Hire<br>Us</h2>
    <div class="label label--pros"><sup>+</sup>Advantages</div>
    <ul class="points points--pros"><li>Gain the full benefits of our experience</li><li>Have a team of Family Law focus attorneys</li><li>Often saves you or makes you money in the long run</li><li>Save you time, energy and stress</li></ul>
    <div class="label label--cons">- Disadvantages</div>
    <ul class="points points--cons"><li>Initial cost</li></ul>
  </section>
</main>
</body>
</html>
```